Flyer for Photo booth business for wedding expo

Hi the flyer is for velvet lantern photo booth rentals.
We are wanting a flyer for a wedding expo this weekend.

1 sided A4

Check out our website for colours etc www.lanternsnapbox.com.au

We are offering 10% discount on Platinum Packages for bookings confirmed within two weeks of the Bridal expo.

Expo Engagement party and Wedding package $1,900.00

Savings of $320.00

3 hour photo booth hire for Engagement package with the funky retro party booth including Props and Logo.

4 hour Platinum Wedding package with Video messaging.

We have a logos and images for the brochure, we are looking for a sleek and fun design with the velvet lantern colours.

www.lanternsnapbox.com.au
info@lanternsnapbox.com.au
0417 263 518

Target Market(s)

potential bride and grooms. partys weddings

Industry/Entity Type

Wedding

Requirements
Must have
• logo and wedding feel
Nice to have
• inventive and creative layout

```html
<!DOCTYPE html>
<html lang="en">
<head>
<meta charset="utf-8">
<title>Velvet Lantern Photo Booth – Bridal Expo Flyer</title>
<link rel="stylesheet" href="https://fonts.googleapis.com/css2?family=Arimo:wght@400;700&family=Arvo:wght@700&family=Cabin+Sketch:wght@700&family=Chewy&family=Playball&display=swap">
<style>
  :root {
    --slate: #3d4249;
    --slate-deep: #2c3036;
    --white: #ffffff;
    --ink: #111111;
    --lime: #a9d24b;
    --orange: #f47a20;
    --yellow: #f2e21a;
    --pink: #e8689a;
    --web-pink: #d2286a;
    --silver: #c9ccd0;
    --silver-dark: #8d9197;
  }
  html, body {
    margin: 0;
    padding: 0;
    width: 849px;
    height: 1200px;
    overflow: hidden;
    background: var(--slate);
  }
  .flyer {
    position: relative;
    width: 849px;
    height: 1200px;
    overflow: hidden;
    background: radial-gradient(ellipse at 40% 40%, #474c54 0%, var(--slate) 55%, var(--slate-deep) 100%);
    font-family: "Arimo", Arial, sans-serif;
    color: var(--white);
  }
  .abs { position: absolute; margin: 0; }

  .ribbon-swoosh { left: 0; top: 0; width: 200px; height: 620px; }

  .tread-plate {
    right: 0; top: 0; width: 250px; height: 250px;
    background: linear-gradient(135deg, #f2f3f5 0%, #b9bdc2 45%, #7d8288 100%);
    clip-path: polygon(30% 0, 100% 0, 100% 70%, 78% 100%, 52% 42%);
  }

  .brand-name {
    left: 100px; top: 44px;
    font-family: "Arimo", Arial, sans-serif;
    font-weight: 700;
    font-size: 46px;
    line-height: 50px;
    color: var(--lime);
    letter-spacing: 1px;
  }
  .brand-name span { display: block; font-size: 40px; padding-left: 90px; }

  .mascot {
    left: 528px; top: 44px; width: 118px; height: 118px;
    border-radius: 50%;
    background: radial-gradient(circle, #a7784a 0%, #6e4a2c 100%);
  }
  .camera-art {
    left: 555px; top: 165px; width: 142px; height: 115px;
    border-radius: 14px;
    background: linear-gradient(160deg, #e6e8ea 0%, #9ca1a7 60%, #55595f 100%);
  }

  .offer-banner {
    left: 74px; top: 158px; width: 270px; height: 46px;
    background: var(--white);
    transform: rotate(9deg);
    transform-origin: left center;
    clip-path: polygon(0 10%, 100% 0, 97% 100%, 2% 90%);
  }
  .offer-banner p {
    margin: 0;
    padding: 7px 0 0 12px;
    font-family: "Arvo", Georgia, serif;
    font-weight: 700;
    font-size: 23px;
    color: var(--ink);
    white-space: nowrap;
  }
  .discount {
    left: 340px; top: 172px;
    font-family: "Cabin Sketch", cursive;
    font-weight: 700;
    color: var(--orange);
    transform: rotate(22deg);
    line-height: 1;
    text-align: center;
  }
  .discount .pct { font-size: 40px; display: block; }
  .discount .word { font-size: 26px; display: block; margin-left: 10px; }

  .offer-terms {
    left: 91px; top: 304px; width: 640px;
    font-family: "Cabin Sketch", cursive;
    font-weight: 700;
    font-size: 30px;
    line-height: 40px;
    font-variant: small-caps;
  }

  .package-tag {
    left: 12px; top: 440px;
    font-family: "Chewy", "Comic Sans MS", cursive;
    font-size: 52px;
    line-height: 1;
    color: var(--yellow);
    transform: rotate(-22deg);
  }
  .expo-deal {
    left: 208px; top: 424px;
    font-family: "Arvo", Georgia, serif;
    font-weight: 700;
    font-size: 24px;
    line-height: 34px;
    letter-spacing: 1px;
    text-shadow: -2px -2px 0 var(--ink), 2px -2px 0 var(--ink), -2px 2px 0 var(--ink), 2px 2px 0 var(--ink);
  }
  .expo-deal .saving { color: var(--pink); }

  .package-bar {
    left: 16px; top: 540px; width: 792px; height: 46px;
    background: linear-gradient(180deg, #ffffff 0%, #e4e6e8 100%);
    border-radius: 4px;
  }
  .package-title {
    top: 540px;
    height: 46px;
    font-family: "Playball", cursive;
    font-weight: 400;
    font-size: 32px;
    line-height: 46px;
    letter-spacing: 1px;
    color: var(--ink);
    display: flex;
    align-items: center;
    gap: 10px;
    white-space: nowrap;
  }
  .package-title::before {
    content: "";
    width: 20px; height: 20px;
    border-radius: 50%;
    background: var(--ink);
    flex: none;
  }
  .package-title--wedding { left: 28px; }
  .package-title--engagement { left: 398px; }

  .package-detail {
    font-size: 23px;
    line-height: 30px;
  }
  .package-detail--wedding { left: 76px; top: 606px; width: 260px; text-align: center; }
  .package-detail--engagement { left: 418px; top: 598px; width: 390px; }

  .photo { background: linear-gradient(160deg, #d9d9d9 0%, #8a8a8a 55%, #3a3a3a 100%); }
  .photo--party { left: 28px; top: 696px; width: 378px; height: 202px; clip-path: polygon(0 8%, 100% 0, 100% 100%, 0 92%); }
  .photo--couple { left: 406px; top: 706px; width: 106px; height: 262px; }
  .photo--strip {
    left: 500px; top: 720px; width: 175px; height: 320px;
    border: 10px solid var(--white);
    transform: rotate(28deg);
  }
  .photo--colour {
    left: 91px; top: 900px; width: 250px; height: 186px;
    border: 8px solid var(--white);
    background: linear-gradient(150deg, #f3d36b 0%, #c98f5a 50%, #5c4a3e 100%);
    box-sizing: border-box;
  }
  .camera-art--small {
    left: 668px; top: 906px; width: 160px; height: 150px;
    border-radius: 20px;
    background: linear-gradient(160deg, #6c7077 0%, #2f3237 100%);
  }

  .contact-panel {
    left: 353px; top: 1085px; width: 478px; height: 106px;
    background: linear-gradient(180deg, #ffffff 0%, #d9dcdf 100%);
    border-radius: 18px;
    box-sizing: border-box;
    padding: 10px 0 0 24px;
    color: var(--ink);
    font-style: normal;
  }
  .contact-web {
    display: block;
    font-family: "Arvo", Georgia, serif;
    font-weight: 700;
    font-size: 22px;
    line-height: 30px;
    color: var(--web-pink);
    text-transform: uppercase;
    text-decoration: none;
    margin-bottom: 2px;
  }
  .contact-line {
    display: flex;
    align-items: center;
    gap: 10px;
    font-family: "Arvo", Georgia, serif;
    font-weight: 700;
    font-size: 16px;
    line-height: 26px;
    padding-left: 50px;
  }
  .contact-line svg { width: 20px; height: 20px; flex: none; }
  .contact-button {
    left: 262px; top: 1133px; width: 134px; height: 38px;
    z-index: 2;
    background: var(--orange);
    border-radius: 6px;
    font-size: 20px;
    line-height: 38px;
    text-align: center;
    color: var(--white);
    white-space: nowrap;
  }
</style>
</head>
<body>
<main class="flyer">

  <svg class="abs ribbon-swoosh" viewBox="0 0 200 620" aria-hidden="true">
    <path d="M70 0 C55 80 62 130 110 190 C60 150 40 90 46 0 Z" fill="var(--silver)"/>
    <path d="M18 400 C30 470 28 520 18 620 L6 620 C16 520 18 470 18 400 Z" fill="var(--silver-dark)"/>
  </svg>

  <div class="abs tread-plate" role="img" aria-label="Brushed metal tread plate corner decoration"></div>

  <h1 class="abs brand-name">velvet lantern<span>photo booth</span></h1>
  <div class="abs mascot" role="img" aria-label="Cartoon mascot holding photo prints"></div>
  <div class="abs camera-art" role="img" aria-label="Silver digital camera illustration"></div>

  <div class="abs offer-banner"><p>WE ARE OFFERING</p></div>
  <div class="abs discount"><span class="pct">10%</span><span class="word">DISCOUNT</span></div>

  <p class="abs offer-terms">On Platinum Packages for bookings confirmed within two weeks of the Bridal Expo.</p>

  <div class="abs package-tag">Package</div>
  <div class="abs expo-deal">
    <div>$1,900.00</div>
    <div>Expo Engagement party and Wedding</div>
    <div class="saving">Savings of $320.00</div>
  </div>

  <div class="abs package-bar"></div>
  <h2 class="abs package-title package-title--wedding">Wedding package</h2>
  <h2 class="abs package-title package-title--engagement">Engagement package</h2>

  <p class="abs package-detail package-detail--wedding">4 hour Platinum , with Video messaging.</p>
  <p class="abs package-detail package-detail--engagement">3 hour photo booth hire :::<br>with the funky retro party booth<br>including Props and Logo.</p>

  <div class="abs photo photo--party" role="img" aria-label="Black and white photo of wedding guests in the booth"></div>
  <div class="abs photo photo--couple" role="img" aria-label="Black and white photo of a couple"></div>
  <div class="abs photo photo--strip" role="img" aria-label="Photo booth strip of friends posing"></div>
  <div class="abs photo photo--colour" role="img" aria-label="Colour photo of a couple with party props"></div>
  <div class="abs camera-art camera-art--small" role="img" aria-label="Black camera illustration"></div>

  <address class="abs contact-panel">
    <a class="contact-web" href="#">www.lanternsnapbox.com.au</a>
    <div class="contact-line">
      <svg viewBox="0 0 20 20" aria-hidden="true"><rect x="2" y="4" width="16" height="12" rx="2" fill="none" stroke="#333" stroke-width="1.8"/><path d="M2 5 L10 11 L18 5" fill="none" stroke="#333" stroke-width="1.8"/></svg>
      INFO@LANTERNSNAPBOX.COM.AU
    </div>
    <div class="contact-line">
      <svg viewBox="0 0 20 20" aria-hidden="true"><circle cx="10" cy="10" r="8.5" fill="none" stroke="#333" stroke-width="1.6"/><path d="M7 5 L9 8 L8 9 C9 11 10 12 12 13 L13 12 L15 14 L13 15.5 C9 15 6 11 5.5 7 Z" fill="#333"/></svg>
      0417 263 518
    </div>
  </address>
  <div class="abs contact-button">Contact Us</div>

</main>
</body>
</html>
```